Smart, intuitive SaaS software dashboard design

PactBloom is an innovative modern SaaS (software as a service) solution for contract and meeting management.

What we are looking for is fresh ideas for our dashboard. We do not need web coding or actionable wireframes now – but purely great design ideas from where to continue forward.

How should a modern web software dashboard look like? Fresh, intuitive, easy-to-use, and adaptable for responsive mobile designs. We hope that when the user logs into the service and sees the dashboard, he/she gets a good big picture of the current status of the most important documents of his/hers company.

To get to know the service and see the components, we kindly ask you to register to our service at www.pactbloom-demo.net and to utilize the free trial (30 days) so you can see the existing dashboard live. And also try out how it works. Might help you to get ideas how to improve it.

(The designer we will choose might be offered later on to design some other pages as well (contract view and edit pages, meeting page etc).)

You’ll find additional information in the attachment.

You’ll find more information of the company and the service also at www.pactbloom-demo.net

Target Market(s)

Global

Industry/Entity Type

Business Management

Number of Pages Required

1 page

Font styles to use
Sans Serif

Requirements
Must have
• 1) Clear design idea for us to iterate from, 2) Modern look and feel - elegant & bold at the same time - still with credibility in our target group. And 3) Suitable for dashboard usage - it should it a clear big picture for the user.
• UPDATE:
• Users should see most important things with one glance. Therefore we would like to see AT LEAST these items mentioned below on the first page.
• NOTE: if all these things are visible on the dashboard, the menu list is maybe not needed on the left. (And there might be some icons on the top header with needed settings/inbox features anyway.)
• NOTE2: as explained earlier, the design should be responsive i.e. work without modifications in PC, iPad and mobile (the areas/boxes would just rearrange themselves on top of each other.)
• -First area should be Documents, which would include different document categories: Contracts, Finance & Admin and HR
• -All different types of Meetings could be the next area (upcoming ones clearly visible with date and maybe description, time and location visible also).
• -Reminders and Activity Feed (they might also be together in top of each other, so that Reminder is visible first and Activity feed can be chosen from the tab.)
• -Virtual Datarooms (maybe 1-3 different ones with some analytics for each visible e.g. like usage/visits per day)
• Saved searches in very important list as users can save their most important searches. There are typically many of these, so at least 5 should be visible and then see all button (maybe even more could be visible if they fit on your design)
• My Latest is also important.
• (As explained, Action Required area is NOT needed anymore).
Nice to have
• Surprise us!
Should not have
• Please avoid the boring traditional legacy stuff and the common report dashboards.
• You do not need design a 100% mockup for the techie to continue with. The ideas count.

```html
<!DOCTYPE html>
<html lang="en">
<head>
<meta charset="utf-8">
<title>PactBloom Dashboard</title>
<link rel="stylesheet" href="https://fonts.googleapis.com/css2?family=Roboto:wght@400;500;700&display=swap">
<style>
:root{
  --navy:#343a4e;
  --green:#6cc000;
  --green-dark:#5aa800;
  --page:#eff2f5;
  --side:#f5f8fa;
  --line:#dfe3e8;
  --text:#33384a;
  --muted:#5f6470;
  --white:#ffffff;
}
*{box-sizing:border-box;margin:0;padding:0}
html,body{width:1200px;height:814px;overflow:hidden}
body{font-family:"Roboto",sans-serif;background:var(--page);color:var(--text);position:relative}
svg{display:block}

/* header */
.brand{position:absolute;left:0;top:0;width:252px;height:86px;background:var(--navy);display:flex;align-items:center;padding-left:26px;gap:10px}
.brand-dot{width:22px;height:22px;border-radius:50%;background:var(--green)}
.brand-name{color:var(--white);font-size:21px;font-weight:400;letter-spacing:1px}
.topnav{position:absolute;left:252px;top:0;right:0;height:39px;display:flex;align-items:center;padding-left:34px;gap:0}
.topnav a{display:flex;align-items:center;gap:9px;font-size:13px;color:var(--text);text-decoration:none;width:119px}
.toolbar{position:absolute;left:252px;top:39px;right:0;height:47px;background:var(--white);border-bottom:1px solid var(--line);display:flex;align-items:center}
.my-latest{width:181px;height:100%;background:var(--navy);color:var(--white);display:flex;align-items:center;padding:0 20px 0 28px;font-size:13.5px;gap:12px}
.my-latest span{flex:1}
.search{flex:1;padding-left:14px;font-size:11.5px;color:var(--text)}
.saved{font-size:13px;padding:0 12px;height:100%;display:flex;align-items:center;border-right:1px solid var(--line)}
.type-select{width:146px;height:100%;display:flex;align-items:center;justify-content:space-between;padding:0 30px 0 22px;font-size:12.5px;font-weight:500}
.add-btn{width:47px;height:100%;background:var(--green);display:flex;align-items:center;justify-content:center}

/* documents */
.hero{position:absolute;left:93px;top:110px;width:722px;height:315px;border-radius:3px;background:linear-gradient(120deg,#3a3430 0%,#5d5650 45%,#2f2c2b 100%)}
.doc-card{position:absolute;left:220px;top:143px;width:469px;height:249px;background:rgba(255,255,255,.93);border-radius:3px;overflow:hidden}
.doc-card h2{height:44px;background:var(--green);color:var(--white);font-size:17.5px;font-weight:500;padding:11px 23px}
.doc-tabs{display:flex;height:40px;background:rgba(235,238,241,.9);padding-left:13px}
.doc-tabs li{list-style:none;display:flex;align-items:center;gap:6px;padding:0 12px;font-size:14px;font-weight:500;color:var(--text)}
.doc-tabs li.active{background:var(--white)}
.doc-body{padding:12px 27px}
.doc-body h3{font-size:14px;font-weight:500;margin-bottom:7px}
.doc-body p{font-size:11px;line-height:15.5px;color:var(--text);margin-bottom:14px}
.btn-dark{display:inline-block;background:var(--navy);color:var(--white);font-size:11.5px;padding:8px 21px;border-radius:2px}

/* meetings */
.meetings{position:absolute;left:92px;top:437px;width:722px;height:316px;background:var(--white);border-radius:3px;overflow:hidden}
.meet-head{height:54px;background:var(--green);display:flex;align-items:flex-end;padding-left:28px}
.meet-head .tab{font-size:18px;font-weight:700;color:var(--white);padding:0 12px 14px}
.meet-head .tab.active{background:var(--page);color:var(--green-dark);padding:14px 16px 12px;margin-bottom:2px}
.meeting{height:123px;padding:18px 32px 0 33px;position:relative;border-bottom:1px solid var(--line)}
.meeting:last-child{border-bottom:0}
.meeting h4{font-size:16px;font-weight:500;margin-bottom:6px}
.date{position:absolute;left:33px;top:44px;width:61px;height:61px;background:var(--side);border:1px solid var(--line);text-align:center;padding-top:12px}
.date small{display:block;font-size:11px}
.date b{font-size:20px;font-weight:500}
.meet-info{margin-left:81px;width:470px}
.meet-info p{font-size:11px;line-height:15.5px;margin-bottom:7px}
.meta{display:flex;gap:26px;font-size:11px;align-items:center}
.meta span{display:flex;gap:7px;align-items:center}
.meet-actions{position:absolute;right:28px;top:19px;width:77px}
.meet-actions div{height:25px;border-radius:2px;color:var(--white);font-size:12.5px;display:flex;align-items:center;justify-content:center;margin-bottom:8px}
.see-all{background:var(--green)}
.add{background:var(--navy)}

/* sidebar */
.sidebar{position:absolute;left:889px;top:86px;width:311px;height:728px;background:var(--side);border-left:1px solid var(--line)}
.side-tabs{position:absolute;left:38px;top:23px;width:236px;height:43px;display:flex;border-bottom:1px solid var(--line)}
.side-tabs div{font-size:17px;display:flex;align-items:center}
.side-tabs .active{background:var(--green);color:var(--white);width:129px;justify-content:center}
.side-tabs .idle{padding-left:15px;color:var(--text)}
.reminders{position:absolute;left:35px;top:89px;width:240px;list-style:none}
.reminders li{height:115px;border-bottom:1px solid var(--line);position:relative;padding:10px 0 0 48px}
.reminders li:nth-child(n+2){height:115px;padding-top:16px}
.avatar{position:absolute;left:3px;top:10px;width:35px;height:35px;border-radius:50%;background:radial-gradient(circle at 50% 40%,#c98c6a,#3b2a24)}
.reminders li:nth-child(n+2) .avatar{top:16px}
.reminders p{font-size:13px;line-height:18.5px;color:var(--muted);margin-bottom:8px}
.when{display:flex;align-items:center;gap:5px;font-size:11px;color:var(--text)}
.cal-btn{position:absolute;left:38px;top:552px;width:104px;height:28px;background:var(--navy);color:var(--white);font-size:11px;font-weight:700;display:flex;align-items:center;justify-content:center;gap:9px;border-radius:2px}
</style>
</head>
<body>

<header>
  <div class="brand"><span class="brand-dot"></span><span class="brand-name">PACTBLOOM</span></div>
  <nav class="topnav">
    <a href="#"><svg width="18" height="18" viewBox="0 0 18 18"><circle cx="9" cy="9" r="7" fill="none" stroke="#33384a" stroke-width="2.4" stroke-dasharray="3 2"/><circle cx="9" cy="9" r="3" fill="none" stroke="#33384a" stroke-width="1.8"/></svg>Settings</a>
    <a href="#"><svg width="19" height="16" viewBox="0 0 19 16"><path d="M1 8v7h17V8" fill="none" stroke="#33384a" stroke-width="2"/><path d="M9.5 1v8M6 6l3.5 3.5L13 6" fill="none" stroke="#33384a" stroke-width="2"/></svg>Inbox</a>
    <a href="#"><svg width="18" height="16" viewBox="0 0 18 16"><g fill="#33384a"><rect x="0" y="1" width="3" height="3"/><rect x="0" y="6.5" width="3" height="3"/><rect x="0" y="12" width="3" height="3"/><rect x="5" y="1.5" width="13" height="2"/><rect x="5" y="7" width="13" height="2"/><rect x="5" y="12.5" width="13" height="2"/></g></svg>Features</a>
    <a href="#"><svg width="18" height="10" viewBox="0 0 18 10"><path d="M2 5h14M5 1L1 5l4 4M13 1l4 4-4 4" fill="none" stroke="#33384a" stroke-width="2"/></svg>Anyway</a>
  </nav>
  <div class="toolbar">
    <div class="my-latest">
      <svg width="18" height="18" viewBox="0 0 18 18"><rect x="1" y="6" width="16" height="11" fill="#fff"/><rect x="5" y="1" width="9" height="7" fill="none" stroke="#fff" stroke-width="1.6"/></svg>
      <span>My Latest</span>
      <svg width="12" height="8" viewBox="0 0 12 8"><path d="M1 1l5 5 5-5" fill="none" stroke="#fff" stroke-width="2"/></svg>
    </div>
    <div class="search">Search..</div>
    <div class="saved">Saved searches</div>
    <div class="type-select">CONTRACTS<svg width="11" height="7" viewBox="0 0 11 7"><path d="M1 1l4.5 4.5L10 1" fill="none" stroke="#33384a" stroke-width="2.2"/></svg></div>
    <div class="add-btn"><svg width="16" height="16" viewBox="0 0 16 16"><path d="M8 1v14M1 8h14" stroke="#fff" stroke-width="3.4"/></svg></div>
  </div>
</header>

<main>
  <section class="hero" role="img" aria-label="Photo of a person working at a café table with a tablet"></section>
  <section class="doc-card">
    <h2>Document Categories</h2>
    <ul class="doc-tabs">
      <li>Contracts <svg width="8" height="5" viewBox="0 0 8 5"><path d="M1 1l3 3 3-3" fill="none" stroke="#33384a"/></svg></li>
      <li class="active">Finance <svg width="8" height="5" viewBox="0 0 8 5"><path d="M1 4l3-3 3 3" fill="none" stroke="#33384a"/></svg></li>
      <li>Admin <svg width="8" height="5" viewBox="0 0 8 5"><path d="M1 1l3 3 3-3" fill="none" stroke="#33384a"/></svg></li>
      <li>HR <svg width="8" height="5" viewBox="0 0 8 5"><path d="M1 1l3 3 3-3" fill="none" stroke="#33384a"/></svg></li>
    </ul>
    <div class="doc-body">
      <h3>Administrative Documents</h3>
      <p>Store and organize all your business-critical financial and administrative contracts and documents in one safe place. Set automated reminders to make sure you never miss important deadlines.</p>
      <span class="btn-dark">Learn More</span>
    </div>
  </section>

  <section class="meetings">
    <div class="meet-head"><span class="tab">Meetings</span><span class="tab active">Upcoming</span></div>
    <article class="meeting">
      <h4>Board Meetings</h4>
      <div class="date"><small>Jun</small><b>17</b></div>
      <div class="meet-info">
        <p>Lorem ipsum dolor sit amet, consectetur adipisicing elit, sed do eiusmod tempor incididunt ut labore et dolore magna aliqua. Ut enim ad minim veniam, quis nostrud exercitation.</p>
        <div class="meta">
          <span><svg width="15" height="15" viewBox="0 0 15 15"><circle cx="7.5" cy="7.5" r="6.3" fill="none" stroke="#5f6470" stroke-width="1.5"/><path d="M7.5 4v4h3" fill="none" stroke="#5f6470" stroke-width="1.5"/></svg>3:20pm</span>
          <span><svg width="10" height="14" viewBox="0 0 10 14"><path d="M5 13C2 9 1 7 1 5a4 4 0 018 0c0 2-1 4-4 8z" fill="none" stroke="#5f6470" stroke-width="1.5"/><circle cx="5" cy="5" r="1.5" fill="#5f6470"/></svg>Lindqvistintie 7 (Northwind building).</span>
        </div>
      </div>
      <div class="meet-actions"><div class="see-all">See All</div><div class="add">ADD</div></div>
    </article>
    <article class="meeting">
      <h4>Board Meetings</h4>
      <div class="date"><small>Agu</small><b>16</b></div>
      <div class="meet-info">
        <p>Lorem ipsum dolor sit amet, consectetur adipisicing elit, sed do eiusmod tempor incididunt ut labore et dolore magna aliqua. Ut enim ad minim veniam, quis nostrud exercitation.</p>
        <div class="meta">
          <span><svg width="15" height="15" viewBox="0 0 15 15"><circle cx="7.5" cy="7.5" r="6.3" fill="none" stroke="#5f6470" stroke-width="1.5"/><path d="M7.5 4v4h3" fill="none" stroke="#5f6470" stroke-width="1.5"/></svg>3:20pm</span>
          <span><svg width="10" height="14" viewBox="0 0 10 14"><path d="M5 13C2 9 1 7 1 5a4 4 0 018 0c0 2-1 4-4 8z" fill="none" stroke="#5f6470" stroke-width="1.5"/><circle cx="5" cy="5" r="1.5" fill="#5f6470"/></svg>Lindqvistintie 7 (Northwind building).</span>
        </div>
      </div>
      <div class="meet-actions"><div class="see-all">See All</div><div class="add">ADD</div></div>
    </article>
  </section>
</main>

<aside class="sidebar">
  <div class="side-tabs"><div class="active">Remindres</div><div class="idle">Activty Feed</div></div>
  <ul class="reminders">
    <li><span class="avatar" role="img" aria-label="User avatar photo"></span><p>Price evaluation point:-Mareting Co-operation Agreem ent Ads Ltd</p><span class="when"><svg width="11" height="11" viewBox="0 0 11 11"><rect x="0.5" y="1.5" width="10" height="9" fill="none" stroke="#33384a"/><path d="M0.5 4h10" stroke="#33384a" stroke-width="1.5"/></svg>29-6-2016</span></li>
    <li><span class="avatar" role="img" aria-label="User avatar photo"></span><p>Expiring:- Security services for Harjula Rock event 2016</p><span class="when"><svg width="11" height="11" viewBox="0 0 11 11"><rect x="0.5" y="1.5" width="10" height="9" fill="none" stroke="#33384a"/><path d="M0.5 4h10" stroke="#33384a" stroke-width="1.5"/></svg>1-7-2016</span></li>
    <li><span class="avatar" role="img" aria-label="User avatar photo"></span><p>Expiring:-Cleaning Services Areement 2015</p><span class="when"><svg width="11" height="11" viewBox="0 0 11 11"><rect x="0.5" y="1.5" width="10" height="9" fill="none" stroke="#33384a"/><path d="M0.5 4h10" stroke="#33384a" stroke-width="1.5"/></svg>6-7-2016</span></li>
    <li><span class="avatar" role="img" aria-label="User avatar photo"></span><p>Expiring:-Consultancy Agreement Veridian 2015</p><span class="when"><svg width="11" height="11" viewBox="0 0 11 11"><rect x="0.5" y="1.5" width="10" height="9" fill="none" stroke="#33384a"/><path d="M0.5 4h10" stroke="#33384a" stroke-width="1.5"/></svg>8-7-2016</span></li>
  </ul>
  <div class="cal-btn"><svg width="11" height="11" viewBox="0 0 11 11"><rect x="0.5" y="1.5" width="10" height="9" fill="none" stroke="#fff"/><path d="M0.5 4h10" stroke="#fff" stroke-width="1.5"/></svg>CAIENDAR</div>
</aside>

</body>
</html>
```